Business Card Design Project

We would need a business name card for our online website business, http://www.plimo.com.sg/. We would need to include our website on the name card as well.

Target Market(s)

Adults and kids in Singapore, mainly expatriates

Industry/Entity Type

Business

Font styles to use
Sans Serif

Colors

Designer to choose colors to be used in the design.

Requirements
Must have
• Must include our "plimo" logo and we would like our name card to be printed on light craft paper material

```html
<!DOCTYPE html>
<html lang="en">
<head>
<meta charset="utf-8">
<title>Plimo Business Card</title>
<link href="https://fonts.googleapis.com/css2?family=Exo+2:wght@300;400;500;600&display=swap" rel="stylesheet">
<style>
  :root {
    --backdrop: #e7e3dc;
    --card-cream: #f2efe9;
    --card-white: #ffffff;
    --band-beige: #efebe3;
    --navy: #1b2a6b;
    --ink: #1c1c1c;
    --orange: #ef6a1d;
    --red: #d8232a;
    --tone-teal: #1597ad;
    --tone-red: #e3162d;
    --tone-blue: #0d5fbd;
  }
  * { box-sizing: border-box; margin: 0; padding: 0; }
  html, body {
    width: 1200px; height: 900px; overflow: hidden;
    background: var(--backdrop);
    font-family: "Exo 2", sans-serif;
  }
  .stage { position: relative; width: 1200px; height: 900px; }
  .card {
    position: absolute; left: 290px; width: 620px; height: 355px;
    box-shadow: 0 10px 28px rgba(0,0,0,.18);
    overflow: hidden;
  }
  .card-front { top: 60px; background: var(--card-cream);
    display: flex; align-items: center; justify-content: center; gap: 22px; }
  .front-dot { width: 74px; height: 74px; border-radius: 50%; background: var(--navy); }
  .front-name { font-size: 64px; font-weight: 400; color: var(--navy); letter-spacing: 2px; }

  .card-back { top: 475px; background: var(--card-white); }
  .back-topline { position: absolute; left: 0; top: 0; width: 100%; height: 10px; background: var(--orange); }
  .back-band { position: absolute; left: 0; top: 10px; width: 100%; height: 125px; background: var(--band-beige); }
  .brand { position: absolute; left: 30px; top: 58px; display: flex; align-items: center; gap: 18px; }
  .brand-dot { width: 68px; height: 68px; border-radius: 50%; background: var(--navy); }
  .brand-name { font-size: 50px; font-weight: 400; color: var(--ink); letter-spacing: 2px; }
  .address { position: absolute; left: 385px; top: 22px; font-size: 16px; font-weight: 500;
    color: var(--navy); line-height: 1.1; letter-spacing: .5px; }
  .person { position: absolute; left: 120px; top: 200px; font-size: 21px; font-weight: 600;
    color: var(--navy); letter-spacing: .5px; }
  .divider { position: absolute; left: 362px; top: 150px; }
  .contacts { position: absolute; left: 392px; top: 150px; list-style: none; }
  .contacts li { display: flex; align-items: center; gap: 12px; height: 27px;
    font-size: 18px; color: var(--navy); letter-spacing: .4px; }
  .contacts svg { width: 18px; height: 18px; flex: none; }
  .colour-band {
    position: absolute; left: 0; bottom: 0; width: 620px; height: 56px;
    background: linear-gradient(90deg, var(--tone-teal) 0%, var(--tone-red) 40%, var(--tone-blue) 70%, var(--tone-teal) 100%);
  }
</style>
</head>
<body>
<main class="stage">
  <section class="card card-front" aria-label="Card front">
    <span class="front-dot"></span>
    <span class="front-name">PLIMO</span>
  </section>

  <section class="card card-back" aria-label="Card back">
    <div class="back-topline"></div>
    <div class="back-band"></div>
    <div class="brand">
      <span class="brand-dot"></span>
      <span class="brand-name">PLIMO</span>
    </div>
    <p class="address">18 Harbour<br>Quay#09-05B<br>Singapore 048612</p>
    <p class="person">MARCUS TAN</p>
    <svg class="divider" width="20" height="90" viewBox="0 0 20 90">
      <line x1="2" y1="2" x2="18" y2="88" stroke="var(--orange)" stroke-width="2"/>
    </svg>
    <ul class="contacts">
      <li>
        <svg viewBox="0 0 24 24"><path fill="var(--red)" d="M6.6 10.8a15 15 0 0 0 6.6 6.6l2.2-2.2c.3-.3.7-.4 1-.2 1.1.4 2.3.6 3.6.6.6 0 1 .4 1 1V20c0 .6-.4 1-1 1A17 17 0 0 1 3 4c0-.6.4-1 1-1h3.5c.6 0 1 .4 1 1 0 1.3.2 2.5.6 3.6.1.3 0 .7-.2 1z"/></svg>
        6315 4820
      </li>
      <li>
        <svg viewBox="0 0 24 24"><rect x="2" y="5" width="20" height="14" rx="1.5" fill="var(--red)"/><path d="M3 6l9 7 9-7" fill="none" stroke="#fff" stroke-width="1.6"/></svg>
        hello@plimocorp.com
      </li>
      <li>
        <svg viewBox="0 0 24 24" fill="none" stroke="var(--red)" stroke-width="1.6"><circle cx="12" cy="12" r="9.5"/><ellipse cx="12" cy="12" rx="4" ry="9.5"/><line x1="2.5" y1="12" x2="21.5" y2="12"/><line x1="4" y1="7" x2="20" y2="7"/><line x1="4" y1="17" x2="20" y2="17"/></svg>
        www.plimo.com.sg
      </li>
    </ul>
    <div class="colour-band" role="img" aria-label="Decorative multicoloured stripe band"></div>
  </section>
</main>
</body>
</html>
```